Emergency Medical Training and Events Company Business Needs Business Card Design

We are in need of a business card for our dynamic company expanding its customer base and need to be easily contacted and identified for when we visit with government officials, potential EMS / Fire agencies and county coordinators to arrange for training programs for first responders to better prepare them for critical thinking at critical incidents.

Target Market(s)

EMS/Fire and Event Promoters

Industry/Entity Type

Medical

Contact Information for Business Card

Two cards, comparable designs:

Martin K. Halvey, Principal, m.halvey@rvqtlo.com
Owen Tash, Event and Training Specialist, m.halvey@rvqtlo.com

Font styles to use
Other font styles liked:
• Cambria

Colors

Designer to choose colors to be used in the design.

Requirements
Must have
• Company Logo, Spots for Name, Title, Phone Number, Email, Website
• A bullet list stating that we offer, QRB CPR and First Aid Instructors, Hold the Line Instructors, Event EMS, CME's, MCI Training and Planning. We prefer to have a black background for the card but if you can make a blue or white card stand out we would review that as well.
Should not have
• Tacky logos or special sayings ... simple, elegant, professional is the look we seek

```html
<!DOCTYPE html>
<html lang="en">
<head>
<meta charset="utf-8">
<title>RVQ Solutions of NY – Business Card</title>
<link rel="stylesheet" href="https://fonts.googleapis.com/css2?family=Roboto:wght@400;500&display=swap">
<style>
  :root {
    --navy: #1b1f4f;
    --navy-pattern: #232861;
    --red: #c8191d;
    --white: #ffffff;
    --rule-light: #d9dbe6;
    --backdrop: #dcdcdc;
  }
  * { box-sizing: border-box; margin: 0; padding: 0; }
  html, body { width: 1200px; height: 900px; overflow: hidden; }
  body {
    background: var(--backdrop);
    font-family: "Roboto", Arial, sans-serif;
    color: var(--white);
    position: relative;
  }
  .card {
    position: absolute;
    left: 272px;
    width: 626px;
    height: 358px;
    border-radius: 24px;
    background: var(--navy);
    overflow: hidden;
  }
  .card--front { top: 58px; }
  .card--back { top: 475px; }

  .pattern-field {
    position: absolute;
    inset: 0;
    background: linear-gradient(135deg, var(--navy-pattern), var(--navy) 60%, var(--navy-pattern));
  }

  .brand {
    position: absolute;
    display: flex;
    align-items: center;
    gap: 16px;
  }
  .brand__mark {
    border-radius: 50%;
    background: var(--white);
    flex: none;
  }
  .brand__name {
    font-weight: 500;
    color: var(--white);
    white-space: nowrap;
    letter-spacing: 0.5px;
  }
  .card--front .brand { left: 92px; top: 140px; }
  .card--front .brand__mark { width: 78px; height: 78px; }
  .card--front .brand__name { font-size: 40px; }

  .card--back .brand { left: 26px; top: 30px; }
  .card--back .brand__mark { width: 64px; height: 64px; }
  .card--back .brand__name { font-size: 32px; }

  .tagline-band {
    position: absolute;
    left: 0; right: 0;
    background: var(--red);
    display: flex;
    align-items: center;
    justify-content: center;
    font-size: 20px;
    font-weight: 400;
    white-space: nowrap;
  }
  .card--front .tagline-band { top: 282px; height: 45px; }
  .card--back .tagline-band { top: 313px; height: 30px; }

  .faint-disc {
    position: absolute;
    left: 200px; top: 130px;
    width: 190px; height: 190px;
    border-radius: 50%;
    background: rgba(255,255,255,0.09);
  }

  .services {
    position: absolute;
    left: 24px; top: 110px;
    list-style: none;
    font-size: 11.5px;
    line-height: 19px;
  }
  .services li { display: flex; align-items: center; gap: 7px; white-space: nowrap; }
  .services li::before {
    content: "";
    width: 6px; height: 6px;
    border-radius: 50%;
    background: var(--red);
    flex: none;
  }

  .person {
    position: absolute;
    right: 37px;
    top: 160px;
    text-align: right;
  }
  .person__name {
    color: var(--red);
    font-size: 26px;
    font-weight: 500;
    line-height: 1.1;
    text-transform: uppercase;
  }
  .person__title { font-size: 16px; margin-top: 2px; }

  .rule-red {
    position: absolute;
    left: 0; right: 0; top: 216px;
    height: 2px;
    background: var(--red);
  }
  .rule-light {
    position: absolute;
    left: 0; right: 0; top: 308px;
    height: 3px;
    background: var(--rule-light);
  }

  .contact-list {
    position: absolute;
    left: 20px; top: 237px;
    list-style: none;
    font-size: 14px;
  }
  .contact-list li {
    display: flex;
    align-items: center;
    gap: 6px;
    height: 20.5px;
  }
  .contact-icon { width: 20px; height: 20px; flex: none; }

  .postal {
    position: absolute;
    right: 37px; top: 257px;
    text-align: right;
    font-size: 14px;
    line-height: 20px;
    font-style: normal;
  }
</style>
</head>
<body>

<section class="card card--front">
  <div class="pattern-field" role="img" aria-label="Repeating faint emblem pattern in navy tones"></div>
  <div class="brand">
    <span class="brand__mark"></span>
    <span class="brand__name">RVQ Solutions of NY</span>
  </div>
  <div class="tagline-band">Responder Venues &amp; Quick Training of New York,LLC</div>
</section>

<section class="card card--back">
  <div class="faint-disc"></div>
  <div class="brand">
    <span class="brand__mark"></span>
    <span class="brand__name">RVQ Solutions of NY</span>
  </div>

  <ul class="services">
    <li>QRB CPR and First Aid Instructors</li>
    <li>Hold the Line Instructors</li>
    <li>Event EMS</li>
    <li>CME's</li>
    <li>MCI Training and Planning</li>
  </ul>

  <div class="person">
    <p class="person__name">Martin K.Halvey</p>
    <p class="person__title">Principal</p>
  </div>

  <div class="rule-red"></div>

  <ul class="contact-list">
    <li>
      <svg class="contact-icon" viewBox="0 0 20 20" aria-hidden="true">
        <circle cx="10" cy="10" r="9" fill="none" stroke="#fff" stroke-width="1"/>
        <circle cx="10" cy="10" r="6" fill="#c8191d"/>
        <path d="M7 8.5h6v1.2h-1v2.5H8v-2.5H7z" fill="#fff"/>
      </svg>
      <span>555 014 2290</span>
    </li>
    <li>
      <svg class="contact-icon" viewBox="0 0 20 20" aria-hidden="true">
        <circle cx="10" cy="10" r="9" fill="none" stroke="#fff" stroke-width="1"/>
        <circle cx="10" cy="10" r="6" fill="#c8191d"/>
        <rect x="6.8" y="8" width="6.4" height="4.4" fill="none" stroke="#fff" stroke-width="0.8"/>
        <path d="M6.8 8l3.2 2.4L13.2 8" fill="none" stroke="#fff" stroke-width="0.8"/>
      </svg>
      <span>m.halvey@rvqtlo.com</span>
    </li>
    <li>
      <svg class="contact-icon" viewBox="0 0 20 20" aria-hidden="true">
        <circle cx="10" cy="10" r="9" fill="none" stroke="#fff" stroke-width="1"/>
        <circle cx="10" cy="10" r="6" fill="#c8191d"/>
        <circle cx="10" cy="10" r="3.6" fill="none" stroke="#fff" stroke-width="0.7"/>
        <path d="M6.4 10h7.2M10 6.4v7.2" stroke="#fff" stroke-width="0.7"/>
      </svg>
      <span>www.rvqtlo.com</span>
    </li>
  </ul>

  <address class="postal">
    PO BOX 418<br>
    Harwick NY 12990
  </address>

  <div class="rule-light"></div>
  <div class="tagline-band">Responder Venues &amp; Quick Training of New York,LLC</div>
</section>

</body>
</html>
```